Varn Medical needs bold attention catching website for healthcare professionals(target)

I need a hero page as well as a products and about page for a website of mine. I specialize in orthopedic instruments . Specifically bone drills and saws. This whole company was founded to bring superb quality highly discounted medical instruments. Specifically bone drills, bone saws, k-wires and pins. Two main points should be cost savings and superior quality.

Target Market(s)

healthcare professionals Surgeons and hospital material managers

Number of Pages Required

3 page

Font styles to use
Serif

Colors

Designer to choose colors to be used in the design.

Requirements
Must have
• colors should match logo design

```html
<!DOCTYPE html>
<html lang="en">
<head>
<meta charset="utf-8">
<title>Varn Medical — Orthopedic Instruments</title>
<link rel="stylesheet" href="https://fonts.googleapis.com/css2?family=Roboto:wght@400;500;700&family=Rubik:wght@500;700&display=swap">
<style>
:root{
  --orange:#f7931e;
  --orange-deep:#ef7a12;
  --dark:#1e1e1e;
  --ink:#222;
  --muted:#777;
  --line:#e3e3e3;
  --soft:#f4f4f4;
  --green:#7cb342;
  --teal:#1f8a86;
  --navy:#1d3e6e;
  --white:#fff;
}
*{box-sizing:border-box;margin:0;padding:0}
html,body{width:1200px;height:3077px;overflow:hidden}
body{font-family:"Roboto",Arial,sans-serif;color:var(--ink);background:var(--white);font-size:13px}
.wrap{width:880px;margin:0 auto;position:relative;height:100%}
section,header,nav,footer,.topbar{position:relative;width:1200px}
h2.section-title{font-family:"Rubik","Roboto",sans-serif;font-weight:500;font-size:26px;text-align:center;color:var(--ink);letter-spacing:.5px}
.title-bar{display:block;width:44px;height:4px;margin:12px auto 0;background:linear-gradient(90deg,var(--orange) 55%,var(--dark) 55%)}

/* top bar */
.topbar{height:26px;background:#f2f2f2;font-size:11px;color:#888}
.topbar .wrap{display:flex;align-items:center;justify-content:space-between}
.topbar .contact span{margin-right:18px}
.social{display:flex;gap:10px}
.social i{width:10px;height:10px;border-radius:50%;background:#b5b5b5;display:block}
.social i.first{background:var(--orange)}

/* header */
header{height:87px;background:var(--white)}
header .wrap{display:flex;align-items:center;justify-content:space-between}
.brand{display:flex;align-items:center;gap:8px;font-family:"Rubik",sans-serif;font-weight:700;font-size:24px;color:var(--orange-deep)}
.brand b{width:14px;height:14px;background:var(--orange-deep);display:block}
.search{display:flex;height:32px;width:430px;border:1px solid var(--line)}
.search .cat{width:92px;font-size:11px;color:var(--orange);display:flex;align-items:center;justify-content:center;border-right:1px solid var(--line)}
.search .field{flex:1;font-size:11px;color:#999;display:flex;align-items:center;padding-left:10px}
.search .btn{width:82px;background:var(--orange);color:#fff;font-size:11px;display:flex;align-items:center;justify-content:center}

/* nav */
nav{height:33px;background:var(--dark)}
nav ul{list-style:none;display:flex;height:33px}
nav li{flex:1;color:#fff;font-size:11px;font-weight:500;display:flex;align-items:center;justify-content:center;border-right:1px solid #333}
nav li:first-child{border-left:1px solid #333}

/* hero */
.hero{height:450px;background:linear-gradient(100deg,#f37a17 0%,#f59a3d 45%,#f2811f 100%);overflow:hidden}
.hero h1{position:absolute;left:0;top:150px;font-family:"Rubik",sans-serif;font-weight:700;font-size:33px;line-height:40px;color:#fff}
.hero p{position:absolute;left:0;top:238px;color:#fff;font-size:15px}
.hero .visual{position:absolute;left:505px;top:75px;width:375px;height:270px;border-radius:6px;background:linear-gradient(160deg,rgba(255,255,255,.34),rgba(255,235,215,.22) 60%,rgba(255,255,255,.12))}
.hero .arrow{position:absolute;top:210px;width:22px;height:30px}
.hero .arrow.prev{left:32px}
.hero .arrow.next{right:32px}
.dots{position:absolute;top:400px;left:50%;transform:translateX(-50%);display:flex;gap:8px}
.dots span{width:20px;height:20px;border-radius:50%;background:#fff;color:var(--orange-deep);font-size:10px;font-weight:700;display:flex;align-items:center;justify-content:center}

/* features */
.features{height:199px;background:var(--soft)}
.feature{position:absolute;top:51px;width:280px;height:108px;background:#fff;border:1px solid var(--line)}
.feature .ribbon{position:absolute;top:-10px;left:50%;transform:translateX(-50%);width:170px;height:22px;color:#fff;font-size:11px;font-weight:700;display:flex;align-items:center;justify-content:center;clip-path:polygon(0 0,100% 0,92% 50%,100% 100%,0 100%,8% 50%)}
.feature .body{position:absolute;left:30px;top:44px;display:flex;align-items:center;gap:14px}
.feature strong{display:block;font-size:14px;font-weight:700}
.feature small{display:block;font-size:12px;color:#555;margin-top:2px}
.f1{left:0}.f1 .ribbon{background:var(--green)}.f1 strong{color:var(--green)}
.f2{left:300px}.f2 .ribbon{background:var(--teal)}.f2 strong{color:var(--teal)}
.f3{left:600px}.f3 .ribbon{background:var(--navy)}.f3 strong{color:var(--navy)}

/* products */
.products{height:432px}
.products h2{padding-top:45px}
.card{position:absolute;top:133px;width:202px;height:240px;border:1px solid var(--line);background:#fff;padding:8px}
.card .shot{height:194px;background:#f3f3f3}
.card .name{text-align:center;font-size:12px;margin-top:12px}
.card.active{background:var(--orange);border-color:var(--orange)}
.card.active .shot{background:#fff}
.card.active .name{color:#fff;font-weight:500}
.products .more{position:absolute;right:0;top:238px;width:26px;height:26px;border:1px solid var(--orange);border-radius:3px;display:flex;align-items:center;justify-content:center;background:#fff}

/* about */
.about{height:433px;background:linear-gradient(90deg,#151515,#1f1f1f 55%,#2a2119 80%,#5a3412)}
.about .photo{position:absolute;left:0;top:52px;width:372px;height:320px;border:6px solid #fff;border-radius:8px;background:linear-gradient(135deg,#c9ced3,#eef0f2 50%,#aab2ba)}
.about .text{position:absolute;left:450px;top:48px;width:430px;color:#ddd}
.about h2{font-family:"Rubik",sans-serif;font-weight:500;font-size:25px;color:#fff}
.about h3{font-size:11px;font-weight:700;color:#fff;margin:22px 0 14px;line-height:16px}
.about p{font-size:11px;line-height:18px;margin-bottom:16px}

/* faq */
.faq{height:522px}
.faq h2{padding-top:45px}
.faq-list{position:absolute;top:134px;left:0;width:880px}
.faq-q{height:40px;border:1px solid var(--line);border-top:none;display:flex;align-items:center;justify-content:space-between;padding:0 14px;font-size:12px;color:#444}
.faq-q .plus{color:var(--orange);font-size:24px;font-weight:300}
.faq-q.open{background:var(--orange);color:#fff;border-color:var(--orange)}
.faq-a{background:#f6f6f6;padding:14px;font-size:10.5px;line-height:16px;color:#999;border:1px solid var(--line);border-top:none}

/* news */
.news{height:305px;background:var(--orange)}
.news .intro{position:absolute;left:0;top:48px;width:200px;color:#fff}
.news h2{font-family:"Rubik",sans-serif;font-weight:500;font-size:27px}
.news .intro p{font-size:11px;line-height:16px;margin-top:16px}
.pill{display:inline-flex;margin-top:16px;background:#fff;color:var(--orange);font-size:10px;font-weight:700;padding:6px 14px;border-radius:14px}
.post{position:absolute;top:53px;width:280px;height:172px;background:#fff;display:flex}
.post .thumb{flex:0 0 112px;width:112px;height:172px;position:relative;background:linear-gradient(160deg,#e9ddd0,#c8a88a)}
.post.p2 .thumb{background:linear-gradient(160deg,#6f7d86,#c98a2a)}
.post .date{position:absolute;top:0;left:0;width:26px;height:28px;background:#fff;color:var(--orange);font-size:10px;font-weight:700;text-align:center;line-height:11px;padding-top:3px}
.post .date small{display:block;font-size:7px}
.post .copy{flex:1;padding:14px 12px}
.post h4{font-size:12.5px;line-height:16px;font-weight:700}
.post p{font-size:10.5px;line-height:15px;color:#999;margin-top:12px}

/* certifications */
.certs{height:302px;background:var(--soft)}
.certs h2{padding-top:45px}
.cert{position:absolute;top:133px;width:200px;height:100px;background:#fff;border-radius:3px;display:flex;align-items:center;justify-content:center}
.cert span{width:150px;height:12px;background:#ececec;border-radius:6px}
.certs .nav-btn{position:absolute;top:171px;width:22px;height:22px;border-radius:50%;display:flex;align-items:center;justify-content:center}

/* footer */
footer{height:244px;background:#fff;border-top:1px solid var(--line)}
footer .brand{position:absolute;left:8px;top:58px;font-size:25px}
.foot-about{position:absolute;left:225px;top:38px;width:220px;font-size:10.5px;line-height:18px;color:#666}
.foot-menu{position:absolute;left:525px;top:38px}
.foot-menu h5,.foot-news h5{font-size:12px;font-weight:700;letter-spacing:.5px}
.foot-menu ul{list-style:none;margin-top:8px}
.foot-menu li{font-size:10.5px;line-height:19px;color:#555}
.foot-menu li.current{color:var(--orange)}
.foot-news{position:absolute;left:675px;top:38px;width:205px}
.foot-news .social{margin-bottom:16px;gap:12px}
.foot-news .social i{width:12px;height:12px;background:#666}
.foot-news .social i.first{background:var(--orange)}
.foot-news .email{height:28px;border:1px solid var(--line);margin-top:12px;font-size:10px;color:#999;display:flex;align-items:center;padding-left:8px}
.foot-news .sub{height:28px;background:var(--orange);color:#fff;font-size:10px;font-weight:700;display:flex;align-items:center;justify-content:center;margin-top:8px}
.copyright{height:44px;border-top:1px solid var(--line);font-size:10.5px;color:#888;display:flex;align-items:center;justify-content:center}
</style>
</head>
<body>

<div class="topbar">
  <div class="wrap">
    <div class="contact"><span>Email: info@varnmedical.com</span><span>Call Us: +1 555 010 2040</span></div>
    <div class="social"><i class="first"></i><i></i><i></i><i></i><i></i></div>
  </div>
</div>

<header>
  <div class="wrap">
    <div class="brand"><b></b>Varn Medical</div>
    <div class="search">
      <div class="cat">All Categories ⌄</div>
      <div class="field">Search Product</div>
      <div class="btn">Search</div>
    </div>
  </div>
</header>

<nav>
  <div class="wrap">
    <ul>
      <li>HOME</li><li>ABOUT US</li><li>PRODUCTS ▾</li><li>CERTIFICATIONS</li><li>CATALOGUES</li><li>BLOG</li><li>CONTACT US</li>
    </ul>
  </div>
</nav>

<section class="hero">
  <svg class="arrow prev" viewBox="0 0 22 30"><path d="M16 4 6 15l10 11" fill="none" stroke="#fff" stroke-width="3"/></svg>
  <svg class="arrow next" viewBox="0 0 22 30"><path d="M6 4l10 11L6 26" fill="none" stroke="#fff" stroke-width="3"/></svg>
  <div class="wrap">
    <h1>Best Manufacturer of<br>Orthopedic Instruments</h1>
    <p>With Over 50 years of experience</p>
    <div class="visual" role="img" aria-label="Bone drill, bone saw and a set of surgical pins and wires"></div>
  </div>
  <div class="dots"><span>1</span><span>2</span><span>3</span><span>4</span><span>II</span></div>
</section>

<section class="features">
  <div class="wrap">
    <div class="feature f1">
      <div class="ribbon">SATISFACTION</div>
      <div class="body">
        <svg width="30" height="26" viewBox="0 0 30 26"><path d="M2 14l9 9L28 3" fill="none" stroke="#7cb342" stroke-width="3"/></svg>
        <div><strong>100% SATISFACTION</strong><small>GUARANTEED</small></div>
      </div>
    </div>
    <div class="feature f2">
      <div class="ribbon">SAVINGS</div>
      <div class="body">
        <svg width="26" height="28" viewBox="0 0 26 28"><rect x="3" y="9" width="20" height="17" rx="4" fill="none" stroke="#1f8a86" stroke-width="2.5"/><path d="M8 3h10l-3 6h-4z" fill="#1f8a86"/><text x="13" y="22" font-size="11" font-weight="700" text-anchor="middle" fill="#1f8a86" font-family="Roboto,sans-serif">$</text></svg>
        <div><strong>COST SAVINGS &amp;</strong><small>SUPERIOR QUALITY</small></div>
      </div>
    </div>
    <div class="feature f3">
      <div class="ribbon">CERTIFICATION</div>
      <div class="body">
        <svg width="30" height="28" viewBox="0 0 30 28"><rect x="2" y="3" width="24" height="19" rx="2" fill="none" stroke="#1d3e6e" stroke-width="2.5"/><path d="M7 9h14M7 14h8" stroke="#1d3e6e" stroke-width="2"/><circle cx="21" cy="20" r="4" fill="#1d3e6e"/></svg>
        <div><strong>CERTIFICATION</strong><small>ON ALL ITEMS</small></div>
      </div>
    </div>
  </div>
</section>

<section class="products">
  <div class="wrap">
    <h2 class="section-title">ORTHOPEDIC INSTRUMENTS</h2><span class="title-bar"></span>
    <div class="card active" style="left:0"><div class="shot" role="img" aria-label="Battery bone drill"></div><div class="name">BONE DRILLS</div></div>
    <div class="card" style="left:226px"><div class="shot" role="img" aria-label="Oscillating bone saw"></div><div class="name">BONE SAW</div></div>
    <div class="card" style="left:452px"><div class="shot" role="img" aria-label="Set of K-wires"></div><div class="name">K-WIRES</div></div>
    <div class="card" style="left:678px"><div class="shot" role="img" aria-label="Set of surgical pins"></div><div class="name">PINS</div></div>
    <div class="more"><svg width="10" height="10" viewBox="0 0 10 10"><path d="M3 1l4 4-4 4" fill="none" stroke="#f7931e" stroke-width="1.6"/></svg></div>
  </div>
</section>

<section class="about">
  <div class="wrap">
    <div class="photo" role="img" aria-label="Hands handling orthopedic instruments in an operating room"></div>
    <div class="text">
      <h2>WHO WE ARE</h2>
      <h3>INSTRUMENTS ARE DESIGNED TO BE FLUID IN LAYOUT AND<br>INTUITIVE IN FUNCTION.</h3>
      <p>Lorem ipsum dolor sit amet, consectetur adipisicing elit, sed do eiusmod tempor incididunt ut labore et dolore magna aliqua. Ut enim ad minim veniam, quis nostrud exercitation ullamco laboris nisi ut aliquip ex ea commodo consequat. Duis aute irure dolor in reprehenderit in voluptate velit esse cillum dolore eu fugiat nulla pariatur. Excepteur sint occaecat cupidatat non proident, sunt in culpa qui officia deserunt mollit anim id est laborum.</p>
      <p>Sed ut perspiciatis unde omnis iste natus error sit voluptatem accusantium doloremque laudantium, totam rem aperiam, eaque ipsa quae ab illo inventore veritatis et quasi architecto beatae vitae dicta sunt explicabo. Nemo enim ipsam voluptatem quia voluptas sit aspernatur aut odit aut fugit, sed quia consequuntur</p>
    </div>
  </div>
</section>

<section class="faq">
  <div class="wrap">
    <h2 class="section-title">FREQUENTLY ASKED QUESTIONS?</h2><span class="title-bar"></span>
    <div class="faq-list">
      <div class="faq-q open">How many different types of surgical instrument are there?</div>
      <div class="faq-a">Sed ut perspiciatis unde omnis iste natus error sit voluptatem accusantium doloremque laudantium, totam rem aperiam, eaque ipsa quae ab illo inventore veritatis et quasi architecto beatae vitae dicta sunt explicabo. Nemo enim ipsam voluptatem quia voluptas sit aspernatur aut odit aut fugit, sed quia consequuntur magni dolores eos qui ratione voluptatem sequi nesciunt. Neque porro quisquam est, qui dolorem ipsum quia dolor sit amet, consectetur</div>
      <div class="faq-q">How many different types of surgical instrument are there?<span class="plus">+</span></div>
      <div class="faq-q">How many different types of surgical instrument are there?<span class="plus">+</span></div>
      <div class="faq-q">How many different types of surgical instrument are there?<span class="plus">+</span></div>
      <div class="faq-q">How many different types of surgical instrument are there?<span class="plus">+</span></div>
      <div class="faq-q">How many different types of surgical instrument are there?<span class="plus">+</span></div>
    </div>
  </div>
</section>

<section class="news">
  <div class="wrap">
    <div class="intro">
      <h2>LATEST NEWS</h2>
      <p>Sed ut perspiciatis unde omnis iste natus error sit voluptatem accusantium doloremque laudantium, totam rem aperiam, eaque ipsa quae ab illo inventore veritatis et quasi architecto</p>
      <span class="pill">OUR BLOG ›</span>
    </div>
    <div class="post" style="left:305px">
      <div class="thumb" role="img" aria-label="Surgical instrument held over a knee"><div class="date">10<small>SEPT</small></div></div>
      <div class="copy"><h4>Lorem ipsum dolor sit amet, consectetur adipiscing elit.</h4><p>Duis aute irure dolor in reprehenderit in voluptate velit esse cillum dolore eu fugiat nulla pariatur [...]</p></div>
    </div>
    <div class="post p2" style="left:600px">
      <div class="thumb" role="img" aria-label="Surgical team at work in an operating theatre"><div class="date">10<small>SEPT</small></div></div>
      <div class="copy"><h4>Lorem ipsum dolor sit amet, consectetur adipiscing elit.</h4><p>Duis aute irure dolor in reprehenderit in voluptate velit esse cillum dolore eu fugiat nulla pariatur [...]</p></div>
    </div>
  </div>
</section>

<section class="certs">
  <div class="wrap">
    <h2 class="section-title">CERTIFICATIONS</h2><span class="title-bar"></span>
    <div class="nav-btn" style="left:-12px;background:#1e1e1e"><svg width="8" height="10" viewBox="0 0 8 10"><path d="M6 1 2 5l4 4" fill="none" stroke="#fff" stroke-width="1.8"/></svg></div>
    <div class="cert" style="left:0"><span></span></div>
    <div class="cert" style="left:226px"><span></span></div>
    <div class="cert" style="left:452px"><span></span></div>
    <div class="cert" style="left:680px"><span></span></div>
    <div class="nav-btn" style="right:-12px;background:var(--orange)"><svg width="8" height="10" viewBox="0 0 8 10"><path d="M2 1l4 4-4 4" fill="none" stroke="#fff" stroke-width="1.8"/></svg></div>
  </div>
</section>

<footer>
  <div class="wrap">
    <div class="brand"><b></b>Varn Medical</div>
    <p class="foot-about">Lorem ipsum dolor sit amet, consectetur adipisicing elit, sed do eiusmod tempor incididunt ut labore et dolore magna aliqua. Ut enim ad minim veniam, quis nostrud exercitation ullamco laboris nisi ut aliquip ex ea commodo consequat. Duis aute irure dolor in reprehenderit in voluptate velit esse cillum dolore eu</p>
    <div class="foot-menu">
      <h5>MENU</h5>
      <ul><li class="current">Home</li><li>About</li><li>Products</li><li>Certifications</li><li>Catalogues</li><li>Blog</li><li>Contact</li></ul>
    </div>
    <div class="foot-news">
      <div class="social"><i class="first"></i><i></i><i></i><i></i><i></i></div>
      <h5>NEWSLETTER SIGNUP</h5>
      <div class="email">Enter Email</div>
      <div class="sub">SUBSCRIBE</div>
    </div>
  </div>
</footer>

<div class="copyright">© 2016 Varn Medical | All rights reserved.</div>

</body>
</html>
```